Need Wordpress business website designed for the website Terravaulto.com

Terravaulto.com needs a Wordpress website to connect mineral rights buyers and sellers from across the United States. This website will be a userfriendly listing service. Below is a list of requirements that need to be accomplished for this project.
-Logo design
-5 to 10 pages of SEO content with copy included. 100-200 words per page.
-Responsive Web design.
-User-friendly add listing page and view listing pages. (2 out of the 7-10 pages needed)
1. Home page
This will have short introduction and possible video plugin.
Welcome to TerraVaulto.com. Market your minerals to a large group of investors. By marketing your mineral rights on TerraVaulto.com Investors compete so you get a fair market offer.
Contact: 866-314-9820
info@Terravaulto.com
2. Our Service or About us Page
-Get the best price for your mineral rights and oil and gas royalties
-Market your mineral rights to attract the best price possible
-Connect you to reputable mineral rights buyers
-Help you understand the industry and answer all of your questions
Our representatives are here to answer any questions you may have.
3 Add Listing Page
Add listing page will need the following boxes
First Name:
Last Name:
Phone Number:
Email:
State:
County:
Net Acres:
Price Per Acre:
Leased Producing
Legal Description:
Comments:
4 View Listing Page
View listing Page will need the following info:
First Name:
Last Name:
Phone Number:
Email:
State:
County:
Net Acres:
Price Per Acre:
Leased Producing
Legal Description:
Comments:
View listings page will need the following:
Listing Number
State: Insert drop down box or fill in form
County: Insert drop down box or fill in form
Legal Description: Fill in form
Net Acres: Fill in form
Price: Fill in form
Notes:
Date Listed:
Interested in this listing? Call 866-314-9820 or fill out the contact box below.
Contact Box:
First Name
Last Name
Email
Phone Number
Questions/Comments?
5. Why Sell?
Receive an immediate lump sum cash payment now.
-Minimize your risk. Protect yourself from the uncertainties of the industry. (Falling natural gas prices, Shut-in and poor producing wells, Infrastructure and pipeline delays)
-Lower taxes. Your mineral rights sale will be taxed at 20% while royalty and bonus payments are taxed as ordinary income at 35%
-Estate Planning. Eliminate complicated forms such as maintenance and depletion schedules, division order agreements, and 1099’s.
-Diversify your assets while paying down bad debt
-Utilize the 1031 tax exchange to invest in more property tax free.
6. News
Page with news articles.
-Research on most important Keywords needed for site.
-Implementation of meta data and HTML elements of site.
-Implement robot tags where needed.
- Creation of sitemap and submission to search engines.
Google Analytics
-Intall a website traffic statistics program that provides important information about viewership. Need to track daily visitors, top search engines and referral sites, bounce rate, top landing pages, mobile traffic, etc...
Google webmaster tools
-Install webmaster tools to determine health and technical status of website.
Listing distribution service
-website needs listed with all four major listing data providers. Quandrel, Bruvex, datakettle, and Pellwick.
Video Plugin
-Option to include video greeting and instruction on homepage.
Setup of Social Media Accounts
-Google+, Facebook, and Linkedin Account pages.
Example Webpages:
deedholderhub.com
plainsacreagetrade.com
subsurfacelots.com
bidforacreshares.com
Target Market(s)
Mineral Rights Owners, Landowners, Mineral Rights Buyers, Oil and Gas Owners, Oil and Gas buyers, Oil and Gas Royalty Owners, Oil and Gas Royalty Buyers, Oil and Gas investors, Mineral Rights Investors.
Industry/Entity Type
Oil And Gas
Requirements
Must have
- -contact box on the right side
- -Location information on bottom of site.
- -live chat box plugin
- -listing box with the following drop down boxes
- First Name:
- Last Name:
- Phone Number:
- Email:
- State:
- County:
- Net Acres:
- Price Per Acre:
- Leased? Producing?
- Legal Description:
- Comments:
Nice to have
- Video plugin on Home page

```html
<!DOCTYPE html>
<html lang="en">
<head>
<meta charset="utf-8">
<title>TerraVaulto – Mineral Rights Listings</title>
<link href="https://fonts.googleapis.com/css2?family=Oswald:wght@400;500&family=Roboto:wght@400;500&family=Open+Sans:wght@400;600&display=swap" rel="stylesheet">
<style>
:root{
  --orange:#e0820f;
  --orange-dark:#c96f08;
  --black:#000;
  --ink:#222;
  --text:#333;
  --muted:#666;
  --line:#e2e2e2;
  --panel:#f4f4f4;
  --footer:#f3f4f6;
  --bar:#262626;
  --white:#fff;
}
*{margin:0;padding:0;box-sizing:border-box}
html,body{width:827px;height:1200px;overflow:hidden;background:var(--white)}
body{position:relative;font-family:"Open Sans",sans-serif;color:var(--text)}
.abs{position:absolute}

/* header */
.site-header{position:absolute;left:0;top:0;width:827px;height:122px;background:var(--black)}
.brand{position:absolute;left:68px;top:18px;display:flex;align-items:center;gap:12px}
.brand-mark{width:26px;height:26px;background:var(--orange)}
.brand-name{font-family:"Oswald",sans-serif;font-weight:500;font-size:30px;color:var(--white);letter-spacing:.5px}
.contact-item{position:absolute;top:21px;display:flex;gap:9px;color:var(--white);font-family:"Roboto",sans-serif}
.contact-item .ring{width:28px;height:28px;border:1.5px solid var(--white);border-radius:50%;display:flex;align-items:center;justify-content:center}
.contact-item .label{font-size:11px;line-height:17px}
.contact-item .value{font-size:10px;color:#ddd}
.main-nav{position:absolute;left:174px;top:67px;width:585px;height:37px;background:var(--orange);display:flex;align-items:center;justify-content:space-around;font-family:"Roboto",sans-serif;font-size:10px;color:var(--white);letter-spacing:.3px}

/* hero */
.hero{position:absolute;left:0;top:122px;width:827px;height:381px;
  background:linear-gradient(180deg,#4a4a4e 0%,#6e6560 35%,#b9843f 65%,#d9952d 80%,#5a3d1c 100%)}
.hero-title{position:absolute;left:482px;top:120px;font-family:"Oswald",sans-serif;font-weight:500;color:var(--white);line-height:1.1}
.hero-title .l1{font-size:33px;display:block}
.hero-title .l2{font-size:37px;display:block}
.hero-text{position:absolute;left:483px;top:207px;width:270px;font-size:10.5px;line-height:16px;color:#f1f1f1}
.btn{display:inline-flex;align-items:center;justify-content:center;background:var(--orange);color:var(--white);font-family:"Roboto",sans-serif;font-size:11.5px}
.hero-btn{position:absolute;left:483px;top:247px;width:117px;height:28px}
.slide-arrow{position:absolute;top:211px;width:26px;height:26px;border-radius:50%;background:rgba(0,0,0,.45);display:flex;align-items:center;justify-content:center}

/* features */
.feature{position:absolute;top:530px;width:230px}
.feature-icon{position:absolute;left:0;top:0;width:64px;height:64px;border-radius:50%;background:var(--orange);border:3px solid #f3d7b4;display:flex;align-items:center;justify-content:center}
.feature h3{position:absolute;left:80px;top:2px;font-family:"Roboto",sans-serif;font-weight:400;font-size:12.5px;color:var(--ink)}
.feature p{position:absolute;left:80px;top:22px;width:140px;font-size:7.5px;line-height:14px;color:var(--text)}
.divider{position:absolute;left:68px;top:628px;width:467px;height:1px;background:var(--line)}

/* welcome */
.video{position:absolute;left:69px;top:652px;width:220px;height:169px;border:1px solid #ccc}
.video-frame{width:100%;height:153px;background:linear-gradient(180deg,#8d97a3 0%,#a9b0b8 55%,#384136 75%,#1f2a1e 100%)}
.video-bar{height:15px;background:#ececec;display:flex;align-items:center;gap:6px;padding:0 6px;font-size:4px;color:#444}
.play{position:absolute;left:95px;top:64px;width:38px;height:38px;border-radius:50%;background:rgba(255,255,255,.55);display:flex;align-items:center;justify-content:center}
.welcome h2{position:absolute;left:308px;top:650px;font-family:"Roboto",sans-serif;font-weight:400;font-size:18px;color:var(--ink)}
.welcome p{position:absolute;left:307px;top:680px;width:223px;font-size:7.6px;line-height:14.2px;color:var(--text)}
.welcome .btn{position:absolute;left:308px;top:794px;width:135px;height:28px;font-size:11px}

/* testimonial */
.testimonial h2{position:absolute;left:68px;top:848px;font-family:"Roboto",sans-serif;font-weight:400;font-size:14px;color:var(--ink)}
.avatar{position:absolute;left:71px;top:883px;width:80px;height:80px;border-radius:50%;border:3px solid #eee;background:linear-gradient(160deg,#cfd4da,#7d8794)}
.quote{position:absolute;left:170px;top:880px;width:360px;font-size:7.4px;line-height:13px;color:var(--muted)}
.stars{position:absolute;left:170px;top:929px;font-size:8px;color:var(--orange);letter-spacing:1px}
.stars .off{color:#bbb}
.ago{position:absolute;left:171px;top:948px;font-size:7.5px;color:var(--muted)}

/* offer form */
.offer{position:absolute;left:555px;top:529px;width:204px;height:441px;background:var(--panel)}
.offer-tab{position:absolute;left:0;top:0;width:170px;height:24px;background:var(--ink);color:var(--white);font-family:"Roboto",sans-serif;font-size:10.5px;line-height:24px;padding-left:17px;clip-path:polygon(0 0,92% 0,100% 100%,0 100%)}
.field{position:absolute;left:18px;width:173px;height:24px;background:var(--white);border:1px solid #e0e0e0;font-size:7.5px;color:#444;line-height:22px;padding-left:10px}
.field.tall{height:47px;line-height:14px;padding-top:4px}
.submit{position:absolute;left:4px;top:404px;width:200px;height:37px;background:var(--ink);color:var(--white);font-family:"Roboto",sans-serif;font-size:11px;display:flex;align-items:center;justify-content:center}

/* live chat */
.live-chat{position:absolute;left:794px;top:820px;width:33px;height:103px;background:var(--orange);border-radius:3px 0 0 3px}
.live-chat span{position:absolute;left:9px;top:10px;writing-mode:vertical-rl;font-family:"Oswald",sans-serif;font-size:10.5px;color:var(--white)}

/* footer */
.footer{position:absolute;left:0;top:1000px;width:827px;height:153px;background:var(--footer)}
.map{position:absolute;left:68px;top:18px;width:264px;height:118px;border:1px solid #ddd;background:linear-gradient(135deg,#eef0d9,#f1e4c2 50%,#c9dbe7)}
.footer h4{position:absolute;top:20px;font-family:"Roboto",sans-serif;font-weight:400;font-size:10.5px;color:var(--ink)}
.social{position:absolute;left:377px;top:43px;display:grid;grid-template-columns:repeat(4,22px);gap:6px}
.social span{width:22px;height:22px;background:var(--orange)}
.footer-sep{position:absolute;left:552px;top:0;width:1px;height:153px;background:#e0e2e6}
.address{position:absolute;left:596px;top:38px;width:170px;font-size:8px;line-height:14px;color:#444}
.footer-line{position:absolute;left:598px;display:flex;align-items:center;gap:10px;font-size:7.8px;color:#444}
.bottom-bar{position:absolute;left:0;top:1153px;width:827px;height:47px;background:var(--bar);color:#ddd;font-size:8px;display:flex;align-items:center;justify-content:center}
</style>
</head>
<body>

<header class="site-header">
  <div class="brand"><span class="brand-mark"></span><span class="brand-name">TERRAVAULTO</span></div>
  <div class="contact-item" style="left:477px">
    <span class="ring"><svg width="13" height="13" viewBox="0 0 24 24"><path d="M6.6 10.8a15 15 0 0 0 6.6 6.6l2.2-2.2c.3-.3.7-.4 1-.2 1.1.4 2.3.6 3.6.6.6 0 1 .4 1 1V20c0 .6-.4 1-1 1C10.6 21 3 13.4 3 4c0-.6.4-1 1-1h3.5c.6 0 1 .4 1 1 0 1.3.2 2.5.6 3.6.1.3 0 .7-.2 1z" fill="#fff"/></svg></span>
    <div><div class="label">Call Us Now!</div><div class="value">+1 866-314-9820</div></div>
  </div>
  <div class="contact-item" style="left:618px">
    <span class="ring"><svg width="13" height="10" viewBox="0 0 24 18"><rect x="1" y="1" width="22" height="16" rx="2" fill="none" stroke="#fff" stroke-width="2"/><path d="M1 2l11 8 11-8" fill="none" stroke="#fff" stroke-width="2"/></svg></span>
    <div><div class="label">E - Mail</div><div class="value">info@terravaulto.com</div></div>
  </div>
  <nav class="main-nav">
    <span>HOME</span><span>ADD LISTING</span><span>ABOUT US</span><span>VIEW LISTINGS</span><span>TESTIMONIALS</span><span>EDUCATION</span>
  </nav>
</header>

<section class="hero" role="img" aria-label="Silhouette of an oil pump jack against a cloudy sunset sky">
  <span class="slide-arrow" style="left:22px"><svg width="10" height="12" viewBox="0 0 10 12"><path d="M7 1L2 6l5 5" stroke="#fff" stroke-width="1.6" fill="none"/></svg></span>
  <span class="slide-arrow" style="left:779px"><svg width="10" height="12" viewBox="0 0 10 12"><path d="M3 1l5 5-5 5" stroke="#fff" stroke-width="1.6" fill="none"/></svg></span>
  <h1 class="hero-title"><span class="l1">ADD YOUR MINERAL</span><span class="l2">Rights Listing Below!</span></h1>
  <p class="hero-text">Lorem ipsum dolor sit amet, consectetur adipiscing elit, sed do eiusmod tempor incididunt ut labore et</p>
  <span class="btn hero-btn">More Information</span>
</section>

<div class="feature" style="left:69px">
  <div class="feature-icon"><svg width="26" height="26" viewBox="0 0 24 24"><path d="M22 2L2 10l8 3 3 8z M10 13L22 2" fill="none" stroke="#fff" stroke-width="1.8" stroke-linejoin="round"/></svg></div>
  <h3>ADD LISTING</h3>
  <p>Lorem ipsum dolor sit amet, cotu adipiscing elit. Lorem ipsum Lorem ipsum dolor sit amet.</p>
</div>
<div class="feature" style="left:329px">
  <div class="feature-icon"><svg width="20" height="24" viewBox="0 0 20 24"><rect x="2" y="1" width="16" height="22" fill="none" stroke="#fff" stroke-width="1.6"/><path d="M6 5h2M12 5h2M6 9h2M12 9h2M6 13h2M12 13h2M8 23v-5h4v5" stroke="#fff" stroke-width="1.6" fill="none"/></svg></div>
  <h3>VIEW LISTINGS</h3>
  <p>Lorem ipsum dolor sit amet, cotu adipiscing elit. Lorem ipsum Lorem ipsum dolor sit amet.</p>
</div>
<div class="divider"></div>

<section class="welcome">
  <div class="video">
    <div class="video-frame" role="img" aria-label="Video still of an oil pump jack and storage tanks in a field"></div>
    <span class="play"><svg width="16" height="18" viewBox="0 0 16 18"><path d="M2 1l13 8-13 8z" fill="#fff"/></svg></span>
    <div class="video-bar">
      <svg width="5" height="6" viewBox="0 0 5 6"><path d="M0 0l5 3-5 3z" fill="#333"/></svg>
      <span>00:00/05:03</span>
      <span style="flex:1;height:2px;background:linear-gradient(90deg,#d33 50%,#555 50%)"></span>
      <span style="width:28px;height:2px;background:#d33"></span>
    </div>
  </div>
  <h2>Welcome To TerraVaulto</h2>
  <p>Welcome to TerraVaulto.com. Add your mineral rights or oil and gas royalties to our database where thousands of mineral buyers compete for your mineral rights. Our service has helped many Mineral Owners get top dollar by putting their mineral rights in front of our large market of mineral rights buyers and investors. Click on the Add Listing button above to get started.</p>
  <span class="btn">WATCH MORE VIDEOS</span>
</section>

<section class="testimonial">
  <h2>Customer Testimonial</h2>
  <div class="avatar" role="img" aria-label="Portrait photo of a customer in a suit"></div>
  <p class="quote"><b style="font-size:10px;color:#555">&ldquo;</b>&nbsp; Lorem ipsum dolor sit amet, consectetur adipiscing elit, sed do eiusmod tempor incididunt ut labore et dolore magna aliqua. Ut enim ad minim veniam, quis nostrud exercitation ullamco laboris nisi ut aliquip ex ea commodo consequat. Duis aute irure dolor</p>
  <div class="stars">★★★<span class="off">☆☆</span></div>
  <div class="ago">8 Months Ago <b style="margin-left:10px;font-size:11px;color:#444">&rdquo;</b></div>
</section>

<aside class="offer">
  <div class="offer-tab">REQUEST AN OFFER</div>
  <div class="field" style="top:42px">First Name :</div>
  <div class="field" style="top:72px">Last Name :</div>
  <div class="field" style="top:101px">Phone Number :</div>
  <div class="field" style="top:131px">Email :</div>
  <div class="field" style="top:160px">State :</div>
  <div class="field" style="top:190px">County :</div>
  <div class="field" style="top:219px">Net Acres :</div>
  <div class="field" style="top:249px">Price Per Acre :</div>
  <div class="field" style="top:278px">Leased? &nbsp;&nbsp; Producing? :</div>
  <div class="field" style="top:308px">Legal Description :</div>
  <div class="field tall" style="top:338px">Comments :</div>
  <div class="submit">SUBMIT NOW</div>
</aside>

<div class="live-chat"><span>LIVE CHAT</span>
  <svg class="abs" style="left:7px;top:80px" width="18" height="18" viewBox="0 0 18 18"><circle cx="9" cy="9" r="8" fill="none" stroke="#fff" stroke-width="1.2"/><path d="M6 6l3 3-3 3M9 6l3 3-3 3" fill="none" stroke="#fff" stroke-width="1.2"/></svg>
</div>

<footer class="footer">
  <div class="map" role="img" aria-label="Street map showing the office location"></div>
  <h4 style="left:373px">CONNECT WITH US</h4>
  <div class="social" aria-label="Social media links">
    <span></span><span></span><span></span><span></span><span></span><span></span>
  </div>
  <div class="footer-sep"></div>
  <h4 style="left:596px">CONTACT US</h4>
  <p class="address">TerraVaulto.com 2150 Harlow Ridge Ave #42 Tulsa, Oklahoma 74103</p>
  <div class="footer-line" style="top:76px"><svg width="12" height="12" viewBox="0 0 24 24"><path d="M6.6 10.8a15 15 0 0 0 6.6 6.6l2.2-2.2c.3-.3.7-.4 1-.2 1.1.4 2.3.6 3.6.6.6 0 1 .4 1 1V20c0 .6-.4 1-1 1C10.6 21 3 13.4 3 4c0-.6.4-1 1-1h3.5c.6 0 1 .4 1 1 0 1.3.2 2.5.6 3.6.1.3 0 .7-.2 1z" fill="none" stroke="#3b6fb5" stroke-width="1.6"/></svg>866-314-9820</div>
  <div class="footer-line" style="top:94px"><svg width="13" height="10" viewBox="0 0 24 18"><rect x="1" y="1" width="22" height="16" fill="none" stroke="#3b6fb5" stroke-width="2"/><path d="M1 2l11 8 11-8" fill="none" stroke="#3b6fb5" stroke-width="2"/></svg>info@Terravaulto.com</div>
</footer>

<div class="bottom-bar">©2015 TerraVaulto.com. - All Rights Reserved.</div>

</body>
</html>
```